お客様へのお礼状などに使うポストカードのデザインをお願いします。
インターネット企業らしい、先進的で明るい未来があるイメージ。SEOやインターネット広告をつかい、新たな販路の拡大と営業効率の最適化を提供出来る会社。シンプルで高級感があり、それが安心感にも繋がるイメージ。
お客様に見込み客をあつめることで、売上が継続的にあがるイメージ。おもて面は宛名が書けるように、郵便番号窓も入れてください。ポストカードは横で使用したいです。裏面はロゴやホームページのデザインイメージと関連のあるようにしたいです。
会社名・所在地・電話番号・ファックス番号・URL
黄・オレンジ系
ハガキテンプレートを添付しますのでテンプレートでの納品をお願いします。(WindowsとMac)

スタイリッシュなデザインありがとうございました。

いろいろなデザインをしていただきありがとうございました。結構迷いました。今後もデザインコンペを行ってまいりますのでよろしくお願いいたします。

```html
<!DOCTYPE html>
<html lang="ja">
<head>
<meta charset="utf-8">
<title>サンライズリンク ポストカード</title>
<link href="https://fonts.googleapis.com/css2?family=Noto+Sans+JP:wght@400&display=swap" rel="stylesheet">
<style>
  :root {
    --page-bg: #ffffff;
    --card-bg: #ffffff;
    --card-edge: #d9d9d9;
    --band: #f4b33c;
    --band-light: #f7c25e;
    --band-text: #fff9ec;
    --zip-main: #c8283c;
    --zip-sub: #e48c98;
  }
  * { margin: 0; padding: 0; box-sizing: border-box; }
  html, body {
    width: 909px; height: 1200px; overflow: hidden;
    background: var(--page-bg);
    font-family: "Noto Sans JP", sans-serif;
  }
  .postcard {
    position: absolute; left: 75px; top: 32px;
    width: 768px; height: 1136px;
    background: var(--card-bg);
    border: 1px solid var(--card-edge);
    overflow: hidden;
  }
  .zip-boxes { position: absolute; left: 0; top: 0; }
  .footer-band {
    position: absolute; left: 0; bottom: 0;
    width: 100%; height: 274px;
    background: linear-gradient(160deg, var(--band-light) 0%, var(--band) 55%);
    color: var(--band-text);
    text-align: center;
  }
  .company {
    position: absolute; top: 46px; left: 0; width: 100%;
    display: flex; justify-content: center; align-items: center; gap: 18px;
    font-size: 33px; letter-spacing: 1px; line-height: 1;
  }
  .company-dot {
    width: 30px; height: 30px; border-radius: 50%;
    background: var(--band-text);
  }
  .contact {
    position: absolute; left: 0; width: 100%;
    font-size: 25px; line-height: 1; letter-spacing: 0.5px;
  }
  .contact.address { top: 124px; }
  .contact.phone { top: 163px; }
  .contact.web { top: 202px; }
  .gap { display: inline-block; width: 30px; }
</style>
</head>
<body>
  <div class="postcard">
    <svg class="zip-boxes" width="768" height="220" viewBox="0 0 768 220">
      <g fill="none" stroke="var(--zip-main)" stroke-width="2">
        <rect x="363" y="91" width="44" height="66"/>
        <rect x="416" y="91" width="44" height="66"/>
        <rect x="470" y="91" width="44" height="66"/>
        <line x1="514" y1="124" x2="527" y2="124"/>
      </g>
      <g fill="none" stroke="var(--zip-sub)" stroke-width="1.5">
        <rect x="529" y="92" width="43" height="64"/>
        <rect x="579" y="92" width="43" height="64"/>
        <rect x="632" y="92" width="43" height="64"/>
        <rect x="685" y="92" width="43" height="64"/>
      </g>
    </svg>

    <div class="footer-band">
      <div class="company">
        <span class="company-dot"></span>
        <span class="company-name">株式会社サンライズリンク</span>
      </div>
      <p class="contact address">〒320-0045<span class="gap"></span>栃木県宇都宮市本町 5-21</p>
      <p class="contact phone">TEL. 028-555-0192<span class="gap"></span>FAX. 03-5550-2741</p>
      <p class="contact web">URL.&nbsp; http://www.sunriselink.co.jp/</p>
    </div>
  </div>
</body>
</html>
```